Banner Ad for online campaigns needed

For our company (Flight simulator experience) we are looking for a banner that will be used for our online marketing campaigns.
Skyvane Flight Simulators allow anyone from six years old to experience flying a large passenger jet, accompanied by a trained co-pilot.

---
The idea behind the project:

It's about what our instructors favorite landings or airports are and thus inspire our customers to try those airports and indeed a skyvane flight.

So it could be mira. Instructor. Having our instructor ID displayed.
And then something like.
Fulfil your dream of being a pilot for a day.
My favorite airport is in Hong Kong. Challenging, thrilling and unexpected landing!
For this experience or for a choice of 24000 airports book your skyvane experience today. Skyvane is the ultimate gift for someone special!

would be great if some text is hand written - "so the pilot really says that.."
----
Need two sizes /same motive/
Size:
Square: 250 x 250
Wide skyscraper: 160 x 600
***
looking for a longterm cooperation
***
Attached:
our logo, + some ideas, picture of our ID
DO NOT use this picture and name in the proposal

Target Market(s)

the main audiance are woman who are looking for gifts for their husbands/brothers. they are looking for something extra and not usual.
they want to fullfill their dreams.

Industry/Entity Type

Marketing

Requirements
Must have
• DO NOT use the attached picture and name in the proposal in your final submission!, bring your own ideas

must be super clear that we are a flight simulator experience

Logo/font requirements:
red: PANTONE 485 U | C CMYK 0 | 100 | 100 | 0 RGB 226 | 0 | 26 HTML #E2001A RAL 3020
black: PANTONE PROCESS BLACK U | C CMYK 0 | 0 | 0 | 100 RGB 0 | 0 | 0 HTML #000000 RAL 9005

FUTURA T LIGHT, URW, NORMAL

Should not have
• no game related notes

```html
<!DOCTYPE html>
<html lang="en">
<head>
<meta charset="utf-8">
<title>Skyvane Flight Simulators – Pilot for a Day banners</title>
<link href="https://fonts.googleapis.com/css2?family=Questrial&family=Roboto:wght@400;700;900&family=Roboto+Condensed:wght@700&family=Gochi+Hand&display=swap" rel="stylesheet">
<style>
  :root {
    --brand-red: #e2001a;
    --brand-black: #000000;
    --ink-grey: #3c3c3c;
    --soft-grey: #5a5a5a;
    --frame-grey: #c9c9c9;
    --paper: #ffffff;
    --paper-tint: #f2f2f2;
    --arrow-dark: #5e5e5e;
    --arrow-light: #a3a3a3;
  }
  * { box-sizing: border-box; margin: 0; padding: 0; }
  html, body { width: 941px; height: 1200px; overflow: hidden; background: var(--paper); }
  body { position: relative; font-family: "Roboto", Arial, sans-serif; }

  .banner { position: absolute; overflow: hidden; border: 2px solid var(--frame-grey);
            background: linear-gradient(180deg, var(--paper-tint) 0%, var(--paper) 40%); }
  .banner--skyscraper { left: 50px; top: 37px; width: 295px; height: 1105px; }
  .banner--square { left: 418px; top: 360px; width: 460px; height: 460px; background: var(--paper); }

  .headline { position: absolute; font-family: "Questrial", "Century Gothic", sans-serif; line-height: 1; }
  .headline__big { display: block; color: var(--brand-red); letter-spacing: 1px; }
  .headline__small { display: block; color: var(--ink-grey); letter-spacing: 1px; }

  .banner--skyscraper .headline { left: 0; right: 0; top: 26px; text-align: center; }
  .banner--skyscraper .headline__big { font-size: 92px; }
  .banner--skyscraper .headline__small { font-size: 40px; margin-top: 2px; }

  .banner--square .headline { left: 22px; top: 26px; }
  .banner--square .headline__big { font-size: 88px; }
  .banner--square .headline__small { font-size: 40px; margin-top: 2px; padding-left: 8px; }

  .swoosh { position: absolute; }
  .banner--skyscraper .swoosh { left: 0; top: 330px; width: 295px; height: 90px; }

  .id-badge { position: absolute; border-radius: 10px;
              background: linear-gradient(160deg, #f04b5b 0%, var(--brand-red) 55%, #b80015 100%); }
  .lanyard { position: absolute; background: linear-gradient(90deg, #c40018, #ef2a3c); border-radius: 4px; }

  .banner--skyscraper .lanyard { left: 200px; top: 150px; width: 26px; height: 120px; transform: rotate(38deg); }
  .banner--skyscraper .id-badge { left: 80px; top: 220px; width: 140px; height: 230px; transform: rotate(-6deg); }
  .banner--square .lanyard { left: 390px; top: -20px; width: 26px; height: 110px; transform: rotate(30deg); }
  .banner--square .id-badge { left: 290px; top: 70px; width: 140px; height: 210px; transform: rotate(-6deg); }

  .airport-choice { position: absolute; left: 175px; top: 362px; width: 96px; height: 96px;
                    border-radius: 50%; background: var(--paper); border: 4px solid var(--brand-red);
                    display: flex; flex-direction: column; align-items: center; justify-content: center;
                    text-align: center; font-weight: 700; color: var(--ink-grey);
                    font-size: 12px; line-height: 1.05; transform: rotate(-12deg); }
  .airport-choice__number { color: var(--brand-red); font-size: 24px; font-weight: 900; }

  .pilot-quote { position: absolute; font-family: "Gochi Hand", cursive; color: var(--ink-grey); }
  .banner--skyscraper .pilot-quote { left: 14px; right: 14px; top: 490px; text-align: center; font-size: 24px; line-height: 1.25; }
  .banner--square .pilot-quote { left: 30px; top: 158px; width: 250px; font-size: 19px; line-height: 1.2; }

  .gift-line { position: absolute; left: 0; right: 0; top: 660px; text-align: center;
               font-family: "Roboto Condensed", "Arial Narrow", sans-serif; font-weight: 700;
               font-size: 42px; line-height: 1.15; text-transform: uppercase;
               text-shadow: 2px 2px 2px rgba(0,0,0,0.25); }
  .gift-line__grey { color: var(--soft-grey); }
  .gift-line__red { color: var(--brand-red); }

  .cta { position: absolute; z-index: 2; }
  .cta__label { font-family: "Roboto Condensed", "Arial Narrow", sans-serif; font-weight: 700; fill: var(--paper); }
  .banner--skyscraper .cta { left: 0; top: 868px; width: 295px; height: 92px; }
  .banner--square .cta { left: 0; top: 238px; width: 262px; height: 82px; }

  .brand-footer { position: absolute; left: 0; right: 0; bottom: 0; background: var(--brand-red); color: var(--paper); }
  .banner--skyscraper .brand-footer { top: 940px; padding: 34px 0 0 16px; }
  .banner--square .brand-footer { top: 310px; padding: 22px 0 0 20px; }

  .brand-name { display: flex; align-items: center; gap: 10px; font-weight: 900; line-height: 1; letter-spacing: 1px; }
  .brand-name__dot { width: 14px; height: 14px; border-radius: 50%; background: var(--paper); }
  .banner--skyscraper .brand-name { font-size: 40px; }
  .banner--square .brand-name { font-size: 54px; }

  .brand-tagline { font-weight: 700; text-transform: uppercase; line-height: 1.2; }
  .banner--skyscraper .brand-tagline { font-size: 14px; margin-top: 6px; }
  .banner--square .brand-tagline { font-size: 20px; margin-top: 8px; }

  .brand-url { font-weight: 700; line-height: 1.2; }
  .banner--skyscraper .brand-url { font-size: 26px; margin-top: 12px; }
  .banner--square .brand-url { font-size: 19px; margin-top: 4px; }
</style>
</head>
<body>

<section class="banner banner--skyscraper" aria-label="Skyvane wide skyscraper banner 160 by 600">
  <h1 class="headline">
    <span class="headline__big">PILOT</span>
    <span class="headline__small">FOR A DAY?</span>
  </h1>

  <svg class="swoosh" viewBox="0 0 295 90" aria-hidden="true">
    <path d="M0 70 C 90 20, 200 10, 295 30" fill="none" stroke="var(--brand-red)" stroke-width="6"/>
  </svg>

  <div class="lanyard" role="img" aria-label="Red lanyard strap with metal clip"></div>
  <div class="id-badge" role="img" aria-label="Instructor cabin crew ID badge with portrait photo and name"></div>

  <div class="airport-choice">
    <span>CHOICE<br>OF</span>
    <span class="airport-choice__number">24000</span>
    <span>AIRPORTS</span>
  </div>

  <p class="pilot-quote">“My favorite airport is in Hong Kong. Challenging, thrilling and unexpected landing! ”</p>

  <p class="gift-line">
    <span class="gift-line__grey">Ultimate</span><br>
    <span class="gift-line__red">Gift for</span><br>
    <span class="gift-line__grey">Someone</span><br>
    <span class="gift-line__red">Special!</span>
  </p>

  <svg class="cta" viewBox="0 0 295 92" aria-label="Book now">
    <defs>
      <linearGradient id="ctaFillTall" x1="0" x2="1">
        <stop offset="0" stop-color="var(--arrow-dark)"/>
        <stop offset="1" stop-color="var(--arrow-light)"/>
      </linearGradient>
    </defs>
    <polygon points="0,22 232,22 232,0 295,46 232,92 232,70 0,70" fill="url(#ctaFillTall)"/>
    <text class="cta__label" x="16" y="59" font-size="32">BOOK NOW!</text>
  </svg>

  <footer class="brand-footer">
    <div class="brand-name"><span>SKYVANE</span><span class="brand-name__dot"></span></div>
    <div class="brand-tagline">Flight Simulator Experience</div>
    <div class="brand-url">www.flyskyvane.com</div>
  </footer>
</section>

<section class="banner banner--square" aria-label="Skyvane square banner 250 by 250">
  <h2 class="headline">
    <span class="headline__big">PILOT</span>
    <span class="headline__small">FOR A DAY?</span>
  </h2>

  <div class="lanyard" role="img" aria-label="Red lanyard strap with metal clip"></div>
  <div class="id-badge" role="img" aria-label="Instructor cabin crew ID badge with portrait photo and name"></div>

  <p class="pilot-quote">“My favorite airport is in Hong Kong. Thrilling &amp; unexpected!”</p>

  <svg class="cta" viewBox="0 0 262 82" aria-label="Book now">
    <defs>
      <linearGradient id="ctaFillSquare" x1="0" x2="1">
        <stop offset="0" stop-color="var(--arrow-dark)"/>
        <stop offset="1" stop-color="var(--arrow-light)"/>
      </linearGradient>
    </defs>
    <polygon points="0,20 205,20 205,0 262,41 205,82 205,62 0,62" fill="url(#ctaFillSquare)"/>
    <text class="cta__label" x="14" y="53" font-size="30">BOOK NOW!</text>
  </svg>

  <footer class="brand-footer">
    <div class="brand-name"><span>SKYVANE</span><span class="brand-name__dot"></span></div>
    <div class="brand-tagline">Flight Simulator Experience</div>
    <div class="brand-url">www.flyskyvane.com</div>
  </footer>
</section>

</body>
</html>
```